Real estate investor business card to retire young ;)!

I need a logo design and a business card. I am based in Montreal, Canada. I buy multi-family properties and do lots development. The final design should communicate that I am a problem solver and reliable.

This card will be given to other investors, to potential sellers and industry experts.

Target Market(s)

Real estate community, multi-family owners

Industry/Entity Type

Real Estate Development

Contact Information for Business Card

My name: Lorna Vickery
email: immo.lorna.vickery@quellmail.example
cellphone: (555) 274-3916

Logo Text

Gestion immobilière

Font styles to use
Sans Serif

Colors
3176b5

Requirements
Must have
• Within 1-2 seconds the person who sees my card should know that I buy properties and lot. Areas to for Phone number and email adress. I do not have a business name. The card should simply state my name and what I do. The logo should be remembered by the person who reads my card
Should not have
• Colors too bright. Too much small details. I want something balanced, bold without being agressive.

```html
<!DOCTYPE html>
<html lang="en">
<head>
<meta charset="utf-8">
<title>Lorna Vickery – Real Estate Investor</title>
<link href="https://fonts.googleapis.com/css2?family=Raleway:wght@400;500&family=Open+Sans:wght@400&display=swap" rel="stylesheet">
<style>
  :root {
    --brand-blue: #3176b5;
    --card-blue: #2f76c6;
    --paper: #f4f4f2;
    --backdrop: #e3e2e0;
    --ink: #3a3a3a;
    --ink-soft: #4d4d4d;
    --white: #ffffff;
  }
  * { margin: 0; padding: 0; box-sizing: border-box; }
  html, body { width: 1200px; height: 800px; overflow: hidden; }
  body {
    background: var(--backdrop);
    font-family: "Raleway", sans-serif;
    position: relative;
  }
  .card {
    position: absolute;
    width: 504px;
    height: 288px;
    border-radius: 3px;
    box-shadow: 0 6px 18px rgba(0,0,0,0.12);
  }
  .card--front {
    left: 60px; top: 60px;
    background: var(--card-blue);
    color: var(--white);
    display: flex; flex-direction: column; align-items: center; justify-content: center;
  }
  .card--back {
    left: 636px; top: 300px;
    background: var(--paper);
    display: flex; align-items: center; justify-content: space-between;
    padding: 0 34px;
  }
  .lockup { display: flex; flex-direction: column; align-items: center; }
  .lockup__row { display: flex; align-items: center; gap: 12px; }
  .lockup__mark { width: 14px; height: 14px; background: currentColor; }
  .lockup__name { font-weight: 400; line-height: 1; }
  .lockup__tagline { text-transform: uppercase; font-weight: 400; }

  .card--front .lockup__name { font-size: 40px; }
  .card--front .lockup__tagline { font-size: 12px; letter-spacing: 0.5em; margin-top: 12px; }

  .card--back .lockup { align-items: flex-start; color: var(--brand-blue); }
  .card--back .lockup__row { gap: 8px; }
  .card--back .lockup__mark { width: 10px; height: 10px; }
  .card--back .lockup__name { font-size: 20px; color: var(--ink); }
  .card--back .lockup__tagline { font-size: 7px; letter-spacing: 0.42em; margin-top: 5px; margin-left: 18px; }

  .contact { list-style: none; font-family: "Open Sans", sans-serif; font-size: 11px; color: var(--ink); }
  .contact__item { display: flex; align-items: center; gap: 7px; margin: 6px 0; }
  .contact__icon { width: 12px; height: 12px; color: var(--brand-blue); flex: none; }

  .lockup--showcase {
    position: absolute; left: 60px; top: 600px;
    align-items: flex-start;
  }
  .lockup--showcase .lockup__row { color: var(--brand-blue); }
  .lockup--showcase .lockup__mark { width: 18px; height: 18px; }
  .lockup--showcase .lockup__name { font-size: 44px; color: var(--ink-soft); }
  .lockup--showcase .lockup__tagline { font-size: 14px; letter-spacing: 0.5em; color: var(--brand-blue); margin-top: 12px; }
</style>
</head>
<body>
  <section class="card card--front">
    <div class="lockup">
      <div class="lockup__row">
        <span class="lockup__mark"></span>
        <span class="lockup__name">Lorna Vickery</span>
      </div>
      <span class="lockup__tagline">Real Estate Investor</span>
    </div>
  </section>

  <section class="card card--back">
    <div class="lockup">
      <div class="lockup__row">
        <span class="lockup__mark"></span>
        <span class="lockup__name">Lorna Vickery</span>
      </div>
      <span class="lockup__tagline">Real Estate Investor</span>
    </div>
    <ul class="contact">
      <li class="contact__item">
        <svg class="contact__icon" viewBox="0 0 12 12" aria-hidden="true">
          <rect x="3" y="0.5" width="6" height="11" rx="1" fill="none" stroke="currentColor" stroke-width="1.2"/>
          <circle cx="6" cy="9.5" r="0.7" fill="currentColor"/>
        </svg>
        <span>(555) 274-3916</span>
      </li>
      <li class="contact__item">
        <svg class="contact__icon" viewBox="0 0 12 12" aria-hidden="true">
          <rect x="0.5" y="2.5" width="11" height="7" fill="currentColor"/>
          <path d="M0.5 2.5 L6 6.5 L11.5 2.5" fill="none" stroke="#fff" stroke-width="0.8"/>
        </svg>
        <span>immo.lorna.vickery@quellmail.example</span>
      </li>
    </ul>
  </section>

  <div class="lockup lockup--showcase">
    <div class="lockup__row">
      <span class="lockup__mark"></span>
      <span class="lockup__name">Lorna Vickery</span>
    </div>
    <span class="lockup__tagline">Real Estate Investor</span>
  </div>
</body>
</html>
```